Information Prospectus for education sector

We need to create a 12 page information memorandum reagrding the education an industry snapshot in Australia, This will be sent to investors in Australia and overseas looking to invest into the education sector in Australia.

Target Market(s)

Investors into the education sector

Industry/Entity Type

Education

Font styles to use
Sans Serif

Colors
fbee3d
33a6d7
9bcb3c

```html
<!DOCTYPE html>
<html lang="en">
<head>
<meta charset="utf-8">
<title>International Education Industry Snapshot – Prospectus Spreads</title>
<link href="https://fonts.googleapis.com/css2?family=Oswald:wght@500;600;700&family=Lato:wght@400;700;900&family=Montserrat:wght@700;800&display=swap" rel="stylesheet">
<style>
:root{
  --yellow:#fbee3d;
  --blue:#33a6d7;
  --green:#9bcb3c;
  --navy:#1d2f8c;
  --purple:#6b4fa0;
  --ink:#1b1b1b;
  --stage:#4a4a4a;
  --white:#ffffff;
  --grey:#e9e9e9;
}
*{margin:0;padding:0;box-sizing:border-box}
html,body{width:1200px;height:1200px;overflow:hidden}
body{background:var(--stage);font-family:'Lato',sans-serif;color:var(--ink);position:relative}
.page{position:absolute;background:var(--white);overflow:hidden}
.p1{left:18px;top:52px;width:380px;height:532px;background:var(--blue)}
.p2{left:413px;top:54px;width:377px;height:530px;background:var(--blue)}
.p3{left:806px;top:55px;width:377px;height:529px}
.p4{left:18px;top:621px;width:377px;height:531px}
.p5{left:409px;top:622px;width:381px;height:534px}
.p6{left:801px;top:619px;width:385px;height:539px;background:var(--grey)}
.photo{position:absolute}
.footer{position:absolute;left:0;bottom:0;width:100%;height:24px;background:var(--green);display:flex;align-items:center;padding-left:32px;font-size:6px;font-weight:700;color:var(--white)}
.page-tag{position:absolute;right:0;bottom:0;height:24px;width:64px;background:var(--yellow);clip-path:polygon(22% 0,100% 0,100% 100%,0 100%);font-size:6px;font-weight:900;display:flex;align-items:center;justify-content:flex-end;padding-right:14px;color:var(--ink)}
.brand{position:absolute;left:12px;top:16px;font-family:'Oswald',sans-serif;font-weight:700;font-size:32px;color:var(--white);letter-spacing:.5px}
.cover-title{position:absolute;left:18px;top:308px;font-family:'Oswald',sans-serif;font-weight:700;font-size:40px;line-height:45px;color:var(--white);letter-spacing:.3px}
.cover-rule{position:absolute;left:18px;top:449px;width:190px;height:1px;background:#cfe9f5}
.cover-foot{position:absolute;left:0;bottom:0;width:100%;height:56px;background:var(--yellow);display:flex;align-items:center;padding-left:28px;font-weight:900;font-size:13px}
.intro{position:absolute;left:28px;top:282px;width:325px;color:var(--white);font-size:6.6px;line-height:10.5px;text-align:justify}
.intro p{margin-bottom:9px}
.intro li{list-style:none;margin-bottom:4px}
.intro li::before{content:"▪ ";}
.p3 .head{position:absolute;left:0;top:0;width:100%;height:74px;background:var(--blue);color:var(--white);font-family:'Oswald',sans-serif;font-weight:600;font-size:22px;line-height:27px;text-align:center;padding-top:12px}
.body-text{position:absolute;font-size:6.4px;line-height:10.4px;text-align:justify}
.body-text p{margin-bottom:8px}
.info-box{position:absolute;left:180px;top:272px;width:197px;height:202px;background:var(--green);padding:7px}
.info-inner{width:100%;height:100%;background:#eef0fb}
.green-card{position:absolute;left:36px;top:10px;width:306px;height:204px;background:var(--green);border-radius:30px}
.green-card h4{text-align:center;font-size:7px;font-weight:900;padding-top:29px;color:#333}
.blue-card{position:absolute;left:50px;top:285px;width:279px;height:190px;background:var(--blue);border-radius:30px}
.blue-card h4{text-align:center;font-size:6px;color:var(--white);font-weight:900;padding-top:17px}
.pill{position:absolute;background:var(--green);color:var(--white);border-radius:10px;font-size:6px;text-align:center;line-height:15px}
.note{position:absolute;font-size:5.8px;line-height:8px}
.biz{position:absolute;left:264px;top:479px;font-family:'Oswald',sans-serif;font-weight:500;font-size:11px}
.label{position:absolute;background:var(--yellow);font-family:'Montserrat',sans-serif;font-weight:800;font-size:19px;line-height:24px;padding:8px 10px}
.side-strip{position:absolute;left:395px;top:262px;width:44px;height:234px;background:var(--blue);color:var(--white);font-size:7px;writing-mode:vertical-rl;display:flex;align-items:center;padding-top:8px}
.p5 .side-strip{left:315px;width:40px}
.panel{position:absolute;left:3px;top:25px;width:243px;height:201px;background:var(--blue);border-radius:2px}
.p6 .text-box{position:absolute;left:0;top:25px;width:225px;height:245px;background:var(--blue);color:var(--white);font-size:6.2px;line-height:7.4px;padding:9px 8px 0 8px;text-align:justify}
.text-box p{margin-bottom:8px}
table{border-collapse:collapse;font-size:4.6px;line-height:6px}
th{font-weight:700;color:var(--white);padding:0 2px;text-align:right}
td{padding:0 2px;text-align:right;border-bottom:.4px solid #ccc}
td:first-child,th:first-child{text-align:left}
.tbl{position:absolute;background:var(--white);border:1px solid var(--navy)}
</style>
</head>
<body>

<!-- Cover -->
<section class="page p1">
  <div class="brand">MERIDIAN EDU</div>
  <div class="photo" role="img" aria-label="Photograph of a bright office reception with marble floor and wooden counter" style="left:0;top:60px;width:380px;height:234px;background:linear-gradient(160deg,#8a7561 0%,#c8b59a 40%,#6e5a48 75%,#9aa6ad 100%)"></div>
  <h1 class="cover-title">THE INTERNATIONAL<br>EDUCATION INDUSTRY<br>SNAPSHOT</h1>
  <div class="cover-rule"></div>
  <div class="cover-foot">www.meridianedu.com.au</div>
</section>

<!-- Page 2 -->
<section class="page p2">
  <div class="photo" role="img" aria-label="Black and white photograph of a modern building atrium with stairs and a numbered column" style="left:0;top:0;width:377px;height:263px;background:linear-gradient(135deg,#ededed 0%,#9b9b9b 35%,#3a3a3a 60%,#bdbdbd 100%)"></div>
  <div class="intro">
    <p>MERIDIAN EDU is an independent and Australian owned agency providing premium specialist services to investors, buyers and sellers across the private education markets.</p>
    <p>Our team consists of people with a long-term successful career in the education industry. The team is a knowledgeable and informed group of professionals with a strong commitment and attitude which allows us to professionally drive negotiations.</p>
    <p>In the first six months of 2018, we have successfully completed many transactions in the sale of international education institutes. We currently have investment and acquisition opportunities from $1m to $15m.</p>
    <p style="margin-bottom:4px">Throughout this presentation, prospective investors will have an insight knowledge of:</p>
    <ul>
      <li>The outlook and growth of International Education Industry in Australia</li>
      <li>Investment opportunity of International Education Industry in Australia</li>
      <li>Investment return and risks</li>
    </ul>
  </div>
  <div class="footer">www.meridianedu.com.au</div>
  <div class="page-tag">Page 2</div>
</section>

<!-- Page 3 -->
<section class="page p3">
  <div class="head">International Education Industry<br>in Australia</div>
  <div class="photo" role="img" aria-label="Black and white photograph of a high-rise office tower" style="left:0;top:86px;width:174px;height:390px;background:linear-gradient(180deg,#d4d4d4 0%,#8a8a8a 45%,#555 100%)"></div>
  <div class="body-text" style="left:184px;top:94px;width:183px">
    <p>In 2016-2017, the Education Industry generated $28.6 Billion to the Australian Economy and was the third largest source of export income for Australia after Iron and Coal. It increased 16.1% compared to 2015-2016 Financial Year which was $24.145 Billion. The growth in Education Export has been very sustainable with the average growth of 11% in the last 5 years.</p>
    <p>The higher education sector generated $19.1 billion in export income (68.1% of total on-shore earnings). The VET sector generated $4.8 billion in earnings (17.3% of total), ELICOS was $1.4 billion (5.2%); schools was $1.2 billion (4.4%); and non-award was $981 million (3.5%).</p>
  </div>
  <div class="info-box">
    <div class="info-inner" role="img" aria-label="Infographic with a map of Australian export income by state and icons noting education as the third largest export, jobs supported, and top source countries"></div>
  </div>
  <div class="footer">www.meridianedu.com.au</div>
  <div class="page-tag">Page 3</div>
</section>

<!-- Page 4 -->
<section class="page p4">
  <div class="green-card">
    <h4>Export income by state and territory, 2016-17</h4>
    <div role="img" aria-label="Map of Australia showing export income by state and territory" style="position:absolute;left:38px;top:42px;width:230px;height:140px;background:linear-gradient(120deg,#efe6c4 0%,#bfbfbf 40%,#dce96b 60%,#8fb4d4 100%);border-radius:40% 45% 35% 30%"></div>
  </div>
  <p class="note" style="left:13px;top:220px;width:352px">The International Education Industry is non arguably one of the key forces to drive the Australian Economy for now and in the future.</p>
  <p class="note" style="left:13px;top:245px;width:352px">Australia has established itself as the global leader in the provision of international education. Its comparative strength – that is, the 'Australian Advantage' – has been integral to our performance to this point, and will be key to the sector's future successes.</p>
  <div class="blue-card">
    <h4>Onshore in Australia: Export income from education services</h4>
    <svg style="position:absolute;left:14px;top:30px" width="250" height="120" viewBox="0 0 250 120" aria-label="Bar chart of export income in billions, 2012-13 to 2016-17">
      <g fill="#fff" font-size="4.5" font-family="Lato,sans-serif" font-weight="700">
        <text x="2" y="60" transform="rotate(-90 6 60)">$ billion</text>
        <text x="12" y="9">30.0</text><text x="12" y="25">25.0</text><text x="12" y="41">20.0</text><text x="12" y="57">15.0</text><text x="12" y="73">10.0</text><text x="12" y="89">5.0</text><text x="12" y="105">0.0</text>
      </g>
      <line x1="28" y1="104" x2="245" y2="104" stroke="#fff" stroke-width=".6"/>
      <g fill="#fff">
        <rect x="46" y="50" width="10" height="54"/>
        <rect x="89" y="45" width="10" height="59"/>
        <rect x="132" y="36" width="10" height="68"/>
        <rect x="175" y="27" width="10" height="77"/>
        <rect x="218" y="14" width="10" height="90"/>
      </g>
      <g fill="#fff" font-size="5" font-weight="700" font-family="Lato,sans-serif" text-anchor="middle">
        <text x="51" y="47">16.9</text><text x="94" y="42">18.5</text><text x="137" y="33">21.3</text><text x="180" y="24">24.1</text><text x="223" y="11">28.0</text>
        <text x="51" y="113">2012-13</text><text x="94" y="113">2013-14</text><text x="137" y="113">2014-15</text><text x="180" y="113">2015-16</text><text x="223" y="113">2016-17</text>
      </g>
    </svg>
    <div class="pill" style="left:52px;top:160px;width:170px">Sourced from the Australian Bureau of Statistics</div>
  </div>
  <div class="biz">Business Opportunities</div>
  <div class="footer">www.meridianedu.com.au</div>
  <div class="page-tag">Page 4</div>
</section>

<!-- Page 5 -->
<section class="page p5">
  <div class="panel">
    <div style="position:absolute;left:0;top:-20px;width:190px;height:14px;background:var(--yellow);font-size:6px;font-weight:900;padding:3px 8px">January – December 2017</div>
    <div role="img" aria-label="Infographic of international student numbers, enrolments, top five source countries and education sectors for 2017" style="position:absolute;left:5px;top:-6px;width:233px;height:200px;background:linear-gradient(160deg,#fbf3e2 0%,#f6ead0 100%)"></div>
  </div>
  <div class="label" style="left:226px;top:70px;width:155px">International<br>Student Data</div>
  <p class="note" style="left:15px;top:228px;width:350px;font-size:6.2px">In 2017, there were 799,371 enrolments generated by 624,001 full-fee paying international students in Australia on a student visa. This represented a 12.7% increase on 2016 and compared with an average annual enrolments growth rate of 4.4% per year over the preceding ten years.</p>
  <p style="position:absolute;left:97px;top:276px;font-size:4.6px;font-weight:700">International Student Enrolments in Australia 1994–2017</p>
  <svg style="position:absolute;left:14px;top:290px" width="300" height="200" viewBox="0 0 300 200" aria-label="Stacked bar chart of international student enrolments by sector 1994-2017">
    <defs>
      <linearGradient id="stack" x1="0" y1="1" x2="0" y2="0">
        <stop offset="0" stop-color="#23309c"/><stop offset=".45" stop-color="#23309c"/>
        <stop offset=".45" stop-color="#7a5aa6"/><stop offset=".65" stop-color="#7a5aa6"/>
        <stop offset=".65" stop-color="#3aa5c5"/><stop offset="1" stop-color="#3aa5c5"/>
      </linearGradient>
    </defs>
    <g font-size="3.6" font-family="Lato,sans-serif" fill="#333">
      <text x="2" y="14">900 000</text><text x="2" y="50">700 000</text><text x="2" y="86">500 000</text><text x="2" y="122">300 000</text><text x="2" y="158">100 000</text><text x="12" y="176">0</text>
    </g>
    <line x1="26" y1="175" x2="290" y2="175" stroke="#999" stroke-width=".5"/>
    <g fill="#333" font-size="4"><rect x="70" y="20" width="3" height="3" fill="#23309c"/><text x="75" y="23">Higher Education</text><rect x="70" y="28" width="3" height="3" fill="#7a5aa6"/><text x="75" y="31">ELICOS</text><rect x="70" y="36" width="3" height="3" fill="#3aa5c5"/><text x="75" y="39">Vocational Education</text></g>
    <g fill="url(#stack)">
      <rect x="30" y="155.2" width="6" height="19.8"/><rect x="41" y="152.5" width="6" height="22.5"/><rect x="52" y="149.8" width="6" height="25.2"/><rect x="63" y="148" width="6" height="27"/>
      <rect x="74" y="147.1" width="6" height="27.9"/><rect x="85" y="146.2" width="6" height="28.8"/><rect x="96" y="140.8" width="6" height="34.2"/><rect x="107" y="133.6" width="6" height="41.4"/>
      <rect x="118" y="126.4" width="6" height="48.6"/><rect x="129" y="121" width="6" height="54"/><rect x="140" y="116.5" width="6" height="58.5"/><rect x="151" y="112.9" width="6" height="62.1"/>
      <rect x="162" y="106.6" width="6" height="68.4"/><rect x="173" y="93.1" width="6" height="81.9"/><rect x="184" y="76.9" width="6" height="98.1"/><rect x="195" y="61.6" width="6" height="113.4"/>
      <rect x="206" y="63.4" width="6" height="111.6"/><rect x="217" y="74.2" width="6" height="100.8"/><rect x="228" y="81.4" width="6" height="93.6"/><rect x="239" y="80.5" width="6" height="94.5"/>
      <rect x="250" y="68.8" width="6" height="106.2"/><rect x="261" y="58.9" width="6" height="116.1"/><rect x="272" y="47.2" width="6" height="127.8"/><rect x="283" y="31" width="6" height="144"/>
    </g>
    <g font-size="3" fill="#333" font-family="Lato,sans-serif">
      <text x="29" y="182">1994</text><text x="95" y="182">2000</text><text x="161" y="182">2006</text><text x="227" y="182">2012</text><text x="282" y="182">2017</text>
      <text x="30" y="191">Note: There is a break in series between 2001 and 2002</text>
    </g>
  </svg>
  <div class="side-strip" style="left:315px;top:262px;width:40px;height:220px;justify-content:center">Sourced from The Department of Education and Training Australia</div>
  <div class="footer">www.meridianedu.com.au</div>
  <div class="page-tag">Page 5</div>
</section>

<!-- Page 6 -->
<section class="page p6">
  <div class="photo" role="img" aria-label="Faded grey photograph of business people standing on rising podium steps" style="left:0;top:0;width:385px;height:270px;background:linear-gradient(180deg,#f2f2f2 0%,#cfcfcf 60%,#e4e4e4 100%)"></div>
  <div class="text-box">
    <p>▪ In 2017, The Higher education sector had the largest share of enrolments and commencements (43.8% and 32.9% respectively) in 2017.</p>
    <p>▪ The VET sector accounted for 27.2% of total enrolments and 30.2% of total commencements in 2017. Enrolments and commencements in the sector increased by 16.7% and 16.1% respectively. China was the next largest source country for enrolments with 8.5%, followed by the Republic of Korea (8.1%) and Thailand (8.0%).</p>
    <p>▪ The English Language Intensive Courses for Overseas Students (ELICOS) sector accounted for 19.4% of total enrolments and 25.9% of total commencements in 2017. Enrolments and commencements grew by 3.4% and 2.9% respectively. China was the largest ELICOS market in the period with 29.3% share of enrolments. Brazil with 11.7% was the second largest nationality for ELICOS enrolments followed by Colombia (8.3%) and Thailand (6.6%).</p>
  </div>
  <div class="label" style="left:226px;top:71px;width:159px">International<br>Student Data</div>
  <div class="tbl" style="left:18px;top:262px;width:350px">
    <table style="width:100%">
      <tr style="background:var(--navy)"><th>Sector</th><th>2016</th><th>2017</th><th>Growth</th><th style="background:#f07f1d">2016</th><th style="background:#f07f1d">2017</th><th style="background:#f07f1d">Growth</th></tr>
      <tr><td>Higher Education</td><td>305,486</td><td>350,472</td><td>14.7%</td><td>131,125</td><td>149,940</td><td>14.3%</td></tr>
      <tr><td>VET</td><td>186,533</td><td>217,696</td><td>16.7%</td><td>118,352</td><td>137,405</td><td>16.1%</td></tr>
      <tr><td>ELICOS</td><td>150,272</td><td>155,448</td><td>3.4%</td><td>114,447</td><td>117,806</td><td>2.9%</td></tr>
      <tr><td>Schools</td><td>23,270</td><td>25,762</td><td>10.7%</td><td>12,371</td><td>13,486</td><td>9.0%</td></tr>
      <tr><td>Non-award</td><td>44,044</td><td>49,993</td><td>13.5%</td><td>34,775</td><td>37,043</td><td>6.5%</td></tr>
      <tr style="font-weight:700"><td>Total in Australia</td><td>709,605</td><td>799,371</td><td>12.7%</td><td>411,070</td><td>455,680</td><td>10.9%</td></tr>
    </table>
    <p style="font-size:4.8px;font-weight:700;padding:2px">The Top 5 nationalities contributed 53.0% of Australia's enrolments in all sectors</p>
    <table style="width:100%">
      <tr style="background:var(--navy)"><th>Nationality</th><th>2016</th><th>2017</th><th>Growth</th><th>Share</th><th>Nationality</th><th>2017</th><th>Growth</th></tr>
      <tr><td>China</td><td>195,731</td><td>231,191</td><td>18.1%</td><td>28.9%</td><td>Colombia</td><td>21,628</td><td>26.5%</td></tr>
      <tr><td>India</td><td>77,841</td><td>87,615</td><td>12.6%</td><td>11.0%</td><td>Taiwan</td><td>18,227</td><td>10.8%</td></tr>
      <tr><td>Brazil</td><td>29,347</td><td>36,496</td><td>24.4%</td><td>4.6%</td><td>Sri Lanka</td><td>10,528</td><td>32.0%</td></tr>
      <tr><td>Nepal</td><td>22,684</td><td>35,423</td><td>56.2%</td><td>4.4%</td><td>Spain</td><td>7,729</td><td>19.9%</td></tr>
      <tr><td>Malaysia</td><td>28,295</td><td>32,899</td><td>16.3%</td><td>4.1%</td><td>Bangladesh</td><td>6,565</td><td>11.3%</td></tr>
      <tr style="font-weight:700"><td>All nationalities</td><td>709,605</td><td>799,371</td><td>12.7%</td><td>100.0%</td><td>Saudi Arabia</td><td>6,551</td><td>-18.8%</td></tr>
    </table>
  </div>
  <p class="note" style="left:18px;top:432px;width:350px;font-size:3.8px;line-height:5px">Data source: Provider Registration and International Student Management System. Enrolment and commencement figures cover full-fee paying students on a student visa only.</p>
  <div class="pill" style="left:69px;top:462px;width:245px;background:var(--blue)">Sourced from The Department of Education and Training Australia</div>
  <div class="footer">www.meridianedu.com.au</div>
  <div class="page-tag">Page 6</div>
</section>

</body>
</html>
```